依頼詳細
比較する栄養素が多いので、どうすればお客様に見て頂きやすいか、
スマホで見た時に伝わりやすいかを重視したデザインにしていただきたいです。

添付している「参考画像」のようなグラフにしようと思ったのですが、
横長に作られており、スマホで見ると文字が小さくなって見づらいのではと思い
こちらでデザインを募らせていただく事となりました。

今のLPに差し込んでも違和感のないデザインでお願いします。

なお、今回はデザインのみでコーディングは必要ありません。
サイトURL
https://tovrekline.com/lp/
ページ数
1ページ
希望イメージ
シンプル 複雑
単色 カラフル
暗い 明るい
日常 高級
遊び心 厳粛
未来的 伝統的
女性的 男性的
希望する色
青系、無彩色系
納品ファイル
• 高解像度JPG (.jpg)
• イラストレーター形式 (.ai)
• フォトショップ形式 (.psd)
補足説明
■ 選んだ理由

一番バランスの良いデザインでした。

■ 提案者全員のお礼・コメント

この度は沢山のご提案ありがとうございました。
また機会がございましたら、どうぞよろしくお願いいたします。

```html
<!DOCTYPE html>
<html lang="ja">
<head>
<meta charset="utf-8">
<title>マルチビタミン成分表</title>
<link href="https://fonts.googleapis.com/css2?family=Noto+Sans+JP:wght@400;500;700&display=swap" rel="stylesheet">
<style>
:root{
  --navy:#1b2f6e;
  --green:#d7e6a4;
  --green-line:#b9cf78;
  --peach:#f4d3b6;
  --peach-line:#e2b18a;
  --pink:#f5dbe7;
  --pink-line:#d9a9c0;
  --grid:#c9c9c9;
  --tick:#666;
  --bg:#fff;
}
*{margin:0;padding:0;box-sizing:border-box}
html,body{width:1200px;height:2940px;overflow:hidden;background:var(--bg);font-family:"Noto Sans JP",sans-serif;color:var(--navy)}
.sheet{position:relative;width:1200px;height:2940px}
.title{position:absolute;top:22px;width:100%;text-align:center;font-size:38px;font-weight:700;letter-spacing:2px}
.subtitle{position:absolute;top:74px;width:100%;text-align:center;font-size:18px;font-weight:700;letter-spacing:1px}
.legend{position:absolute;top:104px;left:40px;right:40px;display:flex;gap:26px;font-size:17px;color:#333}
.legend span{display:flex;align-items:center;gap:8px}
.legend i{display:inline-block;width:40px;height:16px;border:1px solid}
.sw-green{background:var(--green);border-color:var(--green-line)!important}
.sw-navy{background:var(--navy);border-color:var(--navy)!important}
.sw-peach{background:var(--peach);border-color:var(--peach-line)!important}
.sw-pink{background:var(--pink);border-color:var(--pink-line)!important}
.charts{position:absolute;top:0;left:0}
.tick{font-size:18px;fill:var(--tick);text-anchor:end}
.axis{stroke:var(--grid);stroke-width:2}
.b-green{fill:var(--green);stroke:var(--green-line);stroke-width:1}
.b-navy{fill:var(--navy)}
.b-peach{fill:var(--peach);stroke:var(--peach-line);stroke-width:1}
.b-pink{fill:var(--pink);stroke:var(--pink-line);stroke-width:1}
.name{font-size:20px;font-weight:500;fill:var(--navy);text-anchor:end}
.unit{font-size:16px;fill:var(--navy);text-anchor:middle}
.extra-label{position:absolute;left:452px;top:2450px;width:330px;height:34px;background:var(--navy);color:#fff;font-size:18px;font-weight:700;display:flex;align-items:center;justify-content:center}
.extra-list{position:absolute;left:800px;top:2450px;width:360px;list-style:none;font-size:18px;color:#333}
.extra-list li{display:flex;justify-content:space-between;height:27px;line-height:26px;border-bottom:1px solid #bbb;padding:0 4px}
</style>
</head>
<body>
<div class="sheet">
  <h1 class="title">マルチビタミン成分表</h1>
  <p class="subtitle">MULTIVITAMIN INGREDIENT LIST</p>
  <div class="legend">
    <span><i class="sw-green"></i>日本人の食事摂取基準(厚労省2020年)</span>
    <span><i class="sw-navy"></i>ヴィタノラボ</span>
    <span><i class="sw-peach"></i>一般市販サプリ</span>
    <span><i class="sw-pink"></i>MLM系高級サプリ</span>
  </div>

  <svg class="charts" width="1200" height="2940" viewBox="0 0 1200 2940">
    <g class="axes">
      <line class="axis" x1="80" y1="150" x2="80" y2="1120"/><line class="axis" x1="80" y1="1120" x2="220" y2="1120"/>
      <line class="axis" x1="260" y1="150" x2="260" y2="1120"/><line class="axis" x1="260" y1="1120" x2="380" y2="1120"/>
      <line class="axis" x1="420" y1="150" x2="420" y2="1120"/><line class="axis" x1="420" y1="1120" x2="540" y2="1120"/>
      <line class="axis" x1="580" y1="150" x2="580" y2="1120"/><line class="axis" x1="580" y1="1120" x2="680" y2="1120"/>
      <line class="axis" x1="710" y1="150" x2="710" y2="1120"/><line class="axis" x1="710" y1="1120" x2="800" y2="1120"/>
      <line class="axis" x1="845" y1="150" x2="845" y2="1120"/><line class="axis" x1="845" y1="1120" x2="1190" y2="1120"/>

      <line class="axis" x1="80" y1="1310" x2="80" y2="2240"/><line class="axis" x1="80" y1="2240" x2="220" y2="2240"/>
      <line class="axis" x1="260" y1="1310" x2="260" y2="2240"/><line class="axis" x1="260" y1="2240" x2="380" y2="2240"/>
      <line class="axis" x1="420" y1="1310" x2="420" y2="2240"/><line class="axis" x1="420" y1="2240" x2="540" y2="2240"/>
      <line class="axis" x1="580" y1="1310" x2="580" y2="2240"/><line class="axis" x1="580" y1="2240" x2="700" y2="2240"/>
      <line class="axis" x1="740" y1="1310" x2="740" y2="2240"/><line class="axis" x1="740" y1="2240" x2="1190" y2="2240"/>
    </g>

    <g>
      <text class="tick" x="74" y="1126">0</text><text class="tick" x="74" y="1006">100</text><text class="tick" x="74" y="886">200</text><text class="tick" x="74" y="766">300</text><text class="tick" x="74" y="646">400</text><text class="tick" x="74" y="526">500</text><text class="tick" x="74" y="406">600</text><text class="tick" x="74" y="286">700</text><text class="tick" x="74" y="166">800</text>
      <text class="tick" x="254" y="1126">0</text><text class="tick" x="254" y="886">500</text><text class="tick" x="254" y="646">1000</text><text class="tick" x="254" y="406">1500</text><text class="tick" x="254" y="166">2000</text>
      <text class="tick" x="414" y="1126">0</text><text class="tick" x="414" y="886">50</text><text class="tick" x="414" y="646">100</text><text class="tick" x="414" y="406">150</text><text class="tick" x="414" y="166">200</text>
      <text class="tick" x="574" y="1126">0</text><text class="tick" x="574" y="966">2</text><text class="tick" x="574" y="806">4</text><text class="tick" x="574" y="646">6</text><text class="tick" x="574" y="486">8</text><text class="tick" x="574" y="326">10</text><text class="tick" x="574" y="166">12</text>
      <text class="tick" x="704" y="1126">0</text><text class="tick" x="704" y="806">10</text><text class="tick" x="704" y="486">20</text><text class="tick" x="704" y="166">30</text>
      <text class="tick" x="839" y="1126">0</text><text class="tick" x="839" y="806">10</text><text class="tick" x="839" y="486">20</text><text class="tick" x="839" y="166">30</text>
    </g>

    <g>
      <text class="tick" x="74" y="2246">0</text><text class="tick" x="74" y="2062">100</text><text class="tick" x="74" y="1878">200</text><text class="tick" x="74" y="1694">300</text><text class="tick" x="74" y="1510">400</text><text class="tick" x="74" y="1326">500</text>
      <text class="tick" x="254" y="2246">0</text><text class="tick" x="254" y="2062">20</text><text class="tick" x="254" y="1878">40</text><text class="tick" x="254" y="1694">60</text><text class="tick" x="254" y="1510">80</text><text class="tick" x="254" y="1326">100</text>
      <text class="tick" x="414" y="2246">0</text><text class="tick" x="414" y="2131">100</text><text class="tick" x="414" y="2016">200</text><text class="tick" x="414" y="1901">300</text><text class="tick" x="414" y="1786">400</text><text class="tick" x="414" y="1671">500</text><text class="tick" x="414" y="1556">600</text><text class="tick" x="414" y="1441">700</text><text class="tick" x="414" y="1326">800</text>
      <text class="tick" x="574" y="2246">0</text><text class="tick" x="574" y="2131">100</text><text class="tick" x="574" y="2016">200</text><text class="tick" x="574" y="1901">300</text><text class="tick" x="574" y="1786">400</text><text class="tick" x="574" y="1671">500</text><text class="tick" x="574" y="1556">600</text><text class="tick" x="574" y="1441">700</text><text class="tick" x="574" y="1326">800</text>
      <text class="tick" x="734" y="2246">0</text><text class="tick" x="734" y="2093">5</text><text class="tick" x="734" y="1939">10</text><text class="tick" x="734" y="1786">15</text><text class="tick" x="734" y="1633">20</text><text class="tick" x="734" y="1479">25</text><text class="tick" x="734" y="1326">30</text>
    </g>

    <g class="bars">
      <rect class="b-green" x="88" y="340" width="18" height="780"/><rect class="b-navy" x="108" y="1000" width="18" height="120"/><rect class="b-peach" x="128" y="1114" width="18" height="6"/><rect class="b-pink" x="148" y="1108" width="18" height="12"/>
      <rect class="b-green" x="268" y="1118" width="18" height="2"/><rect class="b-navy" x="288" y="160" width="18" height="960"/><rect class="b-peach" x="308" y="1117" width="18" height="3"/><rect class="b-pink" x="328" y="352" width="18" height="768"/>
      <rect class="b-green" x="428" y="640" width="18" height="480"/><rect class="b-navy" x="448" y="160" width="18" height="960"/><rect class="b-peach" x="468" y="808" width="18" height="312"/><rect class="b-pink" x="488" y="160" width="18" height="960"/>
      <rect class="b-green" x="588" y="440" width="18" height="680"/><rect class="b-navy" x="608" y="720" width="18" height="400"/><rect class="b-peach" x="628" y="1096" width="18" height="24"/><rect class="b-pink" x="648" y="240" width="18" height="880"/>
      <rect class="b-green" x="716" y="912" width="18" height="208"/><rect class="b-navy" x="736" y="160" width="18" height="960"/><rect class="b-peach" x="756" y="928" width="18" height="192"/><rect class="b-pink" x="776" y="640" width="18" height="480"/>

      <rect class="b-green" x="850" y="1082" width="13" height="38"/><rect class="b-navy" x="863" y="800" width="13" height="320"/><rect class="b-peach" x="876" y="960" width="13" height="160"/><rect class="b-pink" x="889" y="992" width="13" height="128"/>
      <rect class="b-green" x="906" y="1075" width="13" height="45"/><rect class="b-navy" x="919" y="800" width="13" height="320"/><rect class="b-peach" x="932" y="960" width="13" height="160"/><rect class="b-pink" x="945" y="992" width="13" height="128"/>
      <rect class="b-green" x="962" y="704" width="13" height="416"/><rect class="b-navy" x="975" y="480" width="13" height="640"/><rect class="b-pink" x="1001" y="160" width="13" height="960"/>
      <rect class="b-green" x="1018" y="960" width="13" height="160"/><rect class="b-navy" x="1031" y="640" width="13" height="480"/><rect class="b-peach" x="1044" y="960" width="13" height="160"/><rect class="b-pink" x="1057" y="800" width="13" height="320"/>
      <rect class="b-green" x="1074" y="1078" width="13" height="42"/><rect class="b-navy" x="1087" y="800" width="13" height="320"/><rect class="b-peach" x="1100" y="960" width="13" height="160"/><rect class="b-pink" x="1113" y="992" width="13" height="128"/>
      <rect class="b-green" x="1130" y="1043" width="13" height="77"/><rect class="b-navy" x="1143" y="800" width="13" height="320"/><rect class="b-peach" x="1156" y="1024" width="13" height="96"/><rect class="b-pink" x="1169" y="928" width="13" height="192"/>
    </g>

    <g class="bars">
      <rect class="b-green" x="88" y="1798" width="18" height="442"/><rect class="b-navy" x="108" y="1872" width="18" height="368"/><rect class="b-pink" x="148" y="1357" width="18" height="883"/>
      <rect class="b-green" x="268" y="1780" width="18" height="460"/><rect class="b-navy" x="288" y="1780" width="18" height="460"/><rect class="b-pink" x="328" y="1320" width="18" height="920"/>
      <rect class="b-green" x="428" y="1492" width="18" height="748"/><rect class="b-navy" x="448" y="2067" width="18" height="173"/><rect class="b-peach" x="468" y="2234" width="18" height="6"/><rect class="b-pink" x="488" y="1573" width="18" height="667"/>
      <rect class="b-green" x="588" y="1412" width="18" height="828"/><rect class="b-navy" x="608" y="1906" width="18" height="334"/><rect class="b-pink" x="648" y="1814" width="18" height="426"/>

      <rect class="b-green" x="748" y="1995" width="14" height="245"/><rect class="b-navy" x="763" y="2087" width="14" height="153"/><rect class="b-pink" x="793" y="1872" width="14" height="368"/>
      <rect class="b-green" x="810" y="2133" width="14" height="107"/><rect class="b-navy" x="825" y="2209" width="14" height="31"/><rect class="b-pink" x="855" y="2148" width="14" height="92"/>
      <rect class="b-green" x="872" y="1933" width="14" height="307"/><rect class="b-navy" x="887" y="2179" width="14" height="61"/><rect class="b-pink" x="917" y="1933" width="14" height="307"/>
      <rect class="b-green" x="934" y="1473" width="14" height="767"/><rect class="b-navy" x="949" y="1933" width="14" height="307"/><rect class="b-pink" x="979" y="1320" width="14" height="920"/>
      <rect class="b-green" x="996" y="2212" width="14" height="28"/><rect class="b-navy" x="1011" y="2209" width="14" height="31"/><rect class="b-pink" x="1041" y="2209" width="14" height="31"/>
      <rect class="b-green" x="1058" y="1473" width="14" height="767"/><rect class="b-navy" x="1073" y="2117" width="14" height="123"/><rect class="b-pink" x="1103" y="1473" width="14" height="767"/>
      <rect class="b-navy" x="1135" y="2117" width="14" height="123"/>
    </g>

    <g>
      <text class="name" transform="translate(135 1135) rotate(-90)" dy="7">ビタミンA</text><text class="unit" x="135" y="1300">(mcg)</text>
      <text class="name" transform="translate(315 1135) rotate(-90)" dy="7">β-カロテン</text><text class="unit" x="315" y="1300">(mcg)</text>
      <text class="name" transform="translate(475 1135) rotate(-90)" dy="7">ビタミンC</text><text class="unit" x="475" y="1300">(mg)</text>
      <text class="name" transform="translate(635 1135) rotate(-90)" dy="7">ビタミンD</text><text class="unit" x="635" y="1300">(mcg)</text>
      <text class="name" transform="translate(755 1135) rotate(-90)" dy="7">ビタミンE</text><text class="unit" x="755" y="1300">(mg)</text>
      <text class="name" transform="translate(876 1135) rotate(-90)" dy="7">ビタミンB₁</text><text class="unit" x="876" y="1300">(mg)</text>
      <text class="name" transform="translate(932 1135) rotate(-90)" dy="7">ビタミンB₂</text><text class="unit" x="932" y="1300">(mg)</text>
      <text class="name" transform="translate(988 1135) rotate(-90)" dy="7">ナイアシン</text><text class="unit" x="988" y="1300">(mg)</text>
      <text class="name" transform="translate(1044 1135) rotate(-90)" dy="7">パントテン酸</text><text class="unit" x="1044" y="1300">(mg)</text>
      <text class="name" transform="translate(1100 1135) rotate(-90)" dy="7">ビタミンB₆</text><text class="unit" x="1100" y="1300">(mg)</text>
      <text class="name" transform="translate(1156 1135) rotate(-90)" dy="7">ビタミンB₁₂</text><text class="unit" x="1156" y="1300">(mcg)</text>
    </g>

    <g>
      <text class="name" transform="translate(135 2255) rotate(-90)" dy="7">葉酸</text><text class="unit" x="135" y="2410">(mcg)</text>
      <text class="name" transform="translate(315 2255) rotate(-90)" dy="7">ビオチン</text><text class="unit" x="315" y="2410">(mcg)</text>
      <text class="name" transform="translate(475 2255) rotate(-90)" dy="7">カルシウム</text><text class="unit" x="475" y="2410">(mg)</text>
      <text class="name" transform="translate(635 2255) rotate(-90)" dy="7">マグネシウム</text><text class="unit" x="635" y="2410">(mg)</text>
      <text class="name" transform="translate(778 2255) rotate(-90)" dy="7">亜鉛</text><text class="unit" x="778" y="2410">(mg)</text>
      <text class="name" transform="translate(840 2255) rotate(-90)" dy="7">マンガン</text><text class="unit" x="840" y="2410">(mg)</text>
      <text class="name" transform="translate(902 2255) rotate(-90)" dy="7">クロム</text><text class="unit" x="902" y="2410">(mcg)</text>
      <text class="name" transform="translate(964 2255) rotate(-90)" dy="7">セレン</text><text class="unit" x="964" y="2410">(mcg)</text>
      <text class="name" transform="translate(1026 2255) rotate(-90)" dy="7">銅</text><text class="unit" x="1026" y="2410">(mg)</text>
      <text class="name" transform="translate(1088 2255) rotate(-90)" dy="7">モリブデン</text><text class="unit" x="1088" y="2410">(mcg)</text>
      <text class="name" transform="translate(1150 2255) rotate(-90)" dy="7">イノシトール</text><text class="unit" x="1150" y="2410">(mg)</text>
    </g>
  </svg>

  <div class="extra-label">その他ヴィタノラボに含まれる成分</div>
  <ul class="extra-list">
    <li><span>コリン</span><span>4mg</span></li>
    <li><span>L-システイン</span><span>20mg</span></li>
    <li><span>L-トリプトファン</span><span>40mg</span></li>
    <li><span>L-メチオニン</span><span>3mg</span></li>
    <li><span>ルテイン</span><span>3mg</span></li>
    <li><span>リコペン</span><span>1mg</span></li>
    <li><span>ゼアキサンチン</span><span>1mg</span></li>
    <li><span>パイナップル抽出物</span><span>25mg</span></li>
    <li><span>ローズヒップ抽出物</span><span>3mg</span></li>
    <li><span>レモンバイオフラボノイド</span><span>3mg</span></li>
    <li><span>ポリフェノール</span><span>3mg</span></li>
    <li><span>ビタミンP</span><span>10mg</span></li>
    <li><span>コエンザイムQ10</span><span>10mg</span></li>
    <li><span>スピルリナ原末</span><span>3mg</span></li>
    <li><span>パパイヤ抽出物</span><span>25mg</span></li>
    <li><span>緑茶抽出物</span><span>8mg</span></li>
  </ul>
</div>
</body>
</html>
```